Medical VIP club - small design

Please read the specs in a design brief attached. Also we don't have logo in a Vector format and attaching the only version we have.

Industry/Entity Type

Club

```html
<!DOCTYPE html>
<html lang="en">
<head>
<meta charset="utf-8">
<title>Valemed VIP Club</title>
<link rel="stylesheet" href="https://fonts.googleapis.com/css2?family=Arimo:wght@400;700&family=Questrial&display=swap">
<style>
:root{
  --blue:#0a7fcf;
  --blue-dark:#0561a8;
  --blue-light:#1ba7e8;
  --ink:#0b4f9c;
  --white:#ffffff;
  --grey:#6b6b6b;
  --frame:#dcdcdc;
  --orange:#e7870b;
  --green:#1a9a24;
  --gold:#c9a321;
  --red:#d8262a;
  --purple:#9a3aa8;
}
*{margin:0;padding:0;box-sizing:border-box}
html,body{width:1200px;height:889px;overflow:hidden;background:var(--white)}
.stage{
  position:relative;width:1280px;height:948px;
  transform:scale(.9375);transform-origin:0 0;
  font-family:Arimo,Arial,sans-serif;
  background:linear-gradient(180deg,#fff 0,#fff 95px,#6fb7e4 190px,var(--blue) 270px,#58aee3 380px,#dbeefa 480px,#fff 520px,#fff 100%);
}
.abs{position:absolute}
/* header */
.brand{left:156px;top:40px;display:flex;align-items:center;gap:12px}
.brand-dot{width:44px;height:44px;border-radius:50%;background:var(--blue-light)}
.brand-name{font-family:Questrial,sans-serif;font-size:56px;color:var(--blue-dark);line-height:1}
.call{right:145px;top:42px;text-align:right;color:var(--ink);font-family:Questrial,sans-serif}
.call-1{font-size:26px;font-weight:700;line-height:1}
.call-2{font-size:19px;line-height:1.1}
.call-phone{display:flex;align-items:center;justify-content:flex-end;gap:8px;margin-top:2px}
.call-num{font-size:32px;font-weight:700;color:var(--blue)}
/* main frame */
.frame{left:145px;top:132px;width:990px;height:358px;background:var(--white);border:1px solid var(--frame)}
.frame-shadow{left:180px;top:488px;width:920px;height:30px;border-radius:50%;background:radial-gradient(ellipse at 50% 0,rgba(0,0,0,.28),rgba(0,0,0,0) 70%)}
.nav{left:154px;top:140px;width:972px;height:33px;display:flex}
.nav-tab{height:33px;color:var(--white);font-weight:700;font-size:14px;display:flex;align-items:center;justify-content:center;text-shadow:0 1px 1px rgba(0,0,0,.4);border-right:1px solid rgba(255,255,255,.6)}
.t-orange{width:110px;background:linear-gradient(#f4a634,var(--orange) 60%,#b86405)}
.t-blue{width:110px;background:linear-gradient(#3cb1ee,var(--blue) 60%,var(--blue-dark))}
.t-green{width:105px;background:linear-gradient(#3cc043,var(--green) 60%,#0c6b13)}
.t-gold{width:212px;background:linear-gradient(#ecd063,var(--gold) 60%,#8f7210)}
.t-red{width:140px;background:linear-gradient(#f05a5a,var(--red) 60%,#9a1014)}
.t-purple{width:113px;background:linear-gradient(#c667d2,var(--purple) 60%,#6a1f78)}
.t-fill{flex:1;background:linear-gradient(#25a9ea,var(--blue) 60%,var(--blue-dark));border-right:0}
.slide{left:153px;top:181px;width:974px;height:301px;background:linear-gradient(100deg,#b8463b 0,#c1584a 25%,#e9dcb6 45%,#cdb887 60%,#e6ece4 80%,#f3f3ef 100%)}
.dropdown{left:264px;top:174px;width:109px;height:129px;background:rgba(30,30,30,.82);padding:19px 0 0 10px;list-style:none}
.dropdown li{color:var(--white);font-size:12px;font-weight:700;line-height:20px}
.dropdown li::before{content:"▪ "}
.arrow{width:44px;height:44px}
.caption{left:648px;top:367px;width:479px;height:115px;background:rgba(20,20,20,.78);padding:12px 0 0 18px;color:var(--white)}
.caption-title{font-family:Questrial,sans-serif;font-size:31px;letter-spacing:.5px}
.caption-title b{font-weight:700}
.caption-text{font-family:Questrial,sans-serif;font-weight:700;font-size:13.5px;line-height:18px;margin-top:8px;text-transform:uppercase}
/* cards */
.card{top:533px;height:210px;background:var(--white);border:1px solid var(--frame);padding:5px;box-shadow:0 8px 8px -6px rgba(0,0,0,.25)}
.card-photo{height:146px}
.card-label{height:52px;background:linear-gradient(var(--blue-dark),var(--blue-light));color:var(--white);font-family:Questrial,sans-serif;font-size:15px;line-height:15px;padding:11px 0 0 11px;text-transform:uppercase}
.card-label b{display:block}
/* footer */
.footbar{left:145px;top:777px;width:990px;height:84px;background:linear-gradient(#16a4e6,var(--blue) 50%,var(--blue-dark));border:1px solid #27a8e8}
.footnav{left:165px;top:811px;display:flex;gap:12px;list-style:none}
.footnav li{color:var(--white);font-size:12px}
.footnav li::before{content:"▪ "}
.footbrand{left:959px;top:784px;width:169px;height:70px;background:var(--white);border-radius:30px 4px 4px 4px;display:flex;align-items:center;justify-content:center;gap:7px}
.footbrand .brand-dot{width:22px;height:22px}
.footbrand .brand-name{font-size:28px}
.copy{left:165px;top:874px;font-size:12px;color:var(--grey)}
.social{left:958px;top:873px;display:flex;gap:8px}
.social span{width:36px;height:42px;border-radius:6px;background:linear-gradient(#6cb9ea,var(--blue-dark))}
</style>
</head>
<body>
<div class="stage">
  <div class="abs brand"><span class="brand-dot"></span><span class="brand-name">valemed</span></div>
  <div class="abs call">
    <div class="call-1">CALL US</div>
    <div class="call-2">FOR ANY QUERY'S</div>
    <div class="call-phone">
      <svg width="36" height="36" viewBox="0 0 36 36" aria-hidden="true"><circle cx="18" cy="18" r="16" fill="none" stroke="#222" stroke-width="2"/><path d="M13 10c-2 2-2 6 2 11s9 7 11 5l-3-4-3 1c-2-1-4-4-5-6l1-3z" fill="#222"/></svg>
      <span class="call-num">555-010-020</span>
    </div>
  </div>

  <div class="abs frame-shadow"></div>
  <div class="abs frame"></div>
  <nav class="abs nav">
    <div class="nav-tab t-orange">ABOUT US</div>
    <div class="nav-tab t-blue">VIP CLUB</div>
    <div class="nav-tab t-green">SERVICES</div>
    <div class="nav-tab t-gold">PACKEAGES AND PRICES</div>
    <div class="nav-tab t-red">REGISTRATION</div>
    <div class="nav-tab t-purple">CONTACTS</div>
    <div class="nav-tab t-fill"></div>
  </nav>
  <div class="abs slide" role="img" aria-label="Photo of a bright lounge interior with cream sofas and a red wall"></div>
  <ul class="abs dropdown">
    <li>Lorum ipsum</li><li>Lorum ipsum</li><li>Lorum ipsum</li><li>Lorum ipsum</li><li>Lorum ipsum</li>
  </ul>
  <svg class="abs arrow" style="left:180px;top:314px" viewBox="0 0 44 44" aria-hidden="true"><circle cx="22" cy="22" r="21" fill="#d8d8d8" stroke="#fff" stroke-width="2"/><path d="M27 13v18l-12-9z" fill="#555"/></svg>
  <svg class="abs arrow" style="left:1066px;top:301px" viewBox="0 0 44 44" aria-hidden="true"><circle cx="22" cy="22" r="21" fill="#d8d8d8" stroke="#fff" stroke-width="2"/><path d="M17 13v18l12-9z" fill="#555"/></svg>
  <div class="abs caption">
    <div class="caption-title"><b>VIP</b> CLUB</div>
    <div class="caption-text">Lorem ipsum is simply dummy text of the printing and tting<br>industry lorem ipsum has been the industry's .</div>
  </div>

  <div class="abs card" style="left:145px;width:192px">
    <div class="card-photo" role="img" aria-label="Photo of a hospital emergency entrance sign" style="background:linear-gradient(#c9d4dc,#e6b7b9)"></div>
    <div class="card-label"><b>Emergency services</b>plan covers</div>
  </div>
  <div class="abs card" style="left:351px;width:190px">
    <div class="card-photo" role="img" aria-label="Photo of a passenger plane in a blue sky" style="background:linear-gradient(#8fbde0,#cfe3f1)"></div>
    <div class="card-label"><b>Transportation</b>services</div>
  </div>
  <div class="abs card" style="left:555px;width:183px">
    <div class="card-photo" role="img" aria-label="Photo of a hotel facade" style="background:linear-gradient(#9cc4e4,#5d7a96 70%,#8a5a3c)"></div>
    <div class="card-label"><b>Hotel</b>services</div>
  </div>
  <div class="abs card" style="left:752px;width:184px">
    <div class="card-photo" role="img" aria-label="Photo of a team of doctors" style="background:linear-gradient(#eef1f4,#c9d8e6)"></div>
    <div class="card-label"><b>Variety of</b>doctors</div>
  </div>
  <div class="abs card" style="left:950px;width:185px">
    <div class="card-photo" role="img" aria-label="Photo of joined hands" style="background:linear-gradient(#3b4656,#b98a6c 60%,#2a3340)"></div>
    <div class="card-label"><b>Become a</b>member</div>
  </div>

  <div class="abs footbar"></div>
  <ul class="abs footnav">
    <li>About Us</li><li>VIP Club</li><li>Services</li><li>Packeages and prices</li><li>Registration</li><li>Contacts</li>
  </ul>
  <div class="abs footbrand"><span class="brand-dot"></span><span class="brand-name">valemed</span></div>
  <div class="abs copy">© 2010 Valemed. All Rights Reserved.</div>
  <div class="abs social"><span></span><span></span><span></span><span></span></div>
</div>
</body>
</html>
```